Local Chiropractor Needs Up Scale Webdesign

This website needs to have an upscale look with a very modern feel. Below is the information and websites to reference

Add Logo that is attached

Build a color scheme similar to this website image titled "chiro-1"

Must Include these pages in a horizontal menu bar in this order:
Home, Meet Our Staff, Patient Testimonials, Videos, Work Place Wellness, Contact

Build a "classy looking" Make An Appointment Button into the header with the contact info below

Phone Number:
555-314-2760

Address:
4182 Maple Fern Court, #305
Chanhassen, MN 55492

This website needs 4 rotating banners. Please reference a layout similar to this for the banners: http://drkelrom.com/. However design it nicer than this website, this website is very boring and doesn't flow with the colors properly

Below are the description for each banner

Rotating Banner #1
Use Image: Pediatrics
Two lines of text. First line title line, second description. Use Latin text for fill

Rotating Banner #2
Use Image: Aging Gracefully

Rotating Banner #3
Use Image: Pregnancy

Rotating Banner #4
Use Image: Athletics

I'd like to see a free consultation box similar to the "chiro-1" image. Fields to include are: First Name, Last Name, Phone Number, Comments.

For the body, please fill it with latin text. Please design a professional body layout. You can include a box in the right column for the hours

Office Hours
Monday: 8:00-11:00, 2:00-5:00
Tuesday: 8:30-11:00, 2:00-5:30
Wednesday: 8:00-11:00, 2:00-5:00
Thursday: 10:00-12:00, 2:30-5:00
Friday: 8:00-10:00, 1:00-5:00
Saturday: Closed
Sunday: Closed

For the footer please design something similar to the: http://drkelrom.com/

Also include in the Footer: Powered by Brightpath Site Co

Chiropractor

```html
<!DOCTYPE html>
<html lang="en">
<head>
<meta charset="utf-8">
<title>Verdant Vale Chiropractic Health Center</title>
<link href="https://fonts.googleapis.com/css2?family=Questrial&display=swap" rel="stylesheet">
<style>
:root{
  --dark:#1f1f1f;
  --green:#7fad1f;
  --green-deep:#6e9a14;
  --orange:#dc9d2c;
  --text:#555;
  --field:#ececec;
  --white:#fff;
}
*{margin:0;padding:0;box-sizing:border-box}
html,body{width:935px;height:1200px;overflow:hidden}
body{font-family:"Questrial",sans-serif;background:var(--white);position:relative;color:var(--text)}
.abs{position:absolute}
.header{left:0;top:0;width:935px;height:113px;background:var(--dark)}
.brand{left:176px;top:34px;display:flex;align-items:center;gap:8px}
.brand-mark{width:30px;height:30px;border-radius:50%;background:var(--green)}
.brand-name{color:var(--green);font-size:22px;line-height:1}
.brand-sub{color:var(--green);font-size:11px;margin-top:3px}
.social{right:176px;top:20px;display:flex;gap:6px}
.social span{width:8px;height:8px;border-radius:50%;background:var(--orange)}
.appt{right:176px;top:37px;width:166px;border-top:1px solid #444;border-bottom:1px solid #444;padding:4px 0;text-align:right;color:var(--orange);font-size:11px;letter-spacing:.2px}
.appt svg{vertical-align:middle;margin-right:6px}
.contact-line{right:176px;font-size:8px;color:var(--orange);text-align:right}
.contact-line b{font-weight:normal;color:var(--green)}
.nav{left:0;top:113px;width:935px;height:28px;background:var(--green);display:flex;justify-content:center;gap:29px;align-items:center}
.nav a{color:var(--white);text-decoration:none;font-size:10.5px}
.hero{left:0;top:141px;width:935px;height:379px;background:linear-gradient(100deg,#f3f0ec 0%,#f7e9e2 40%,#f1efec 60%,#e9e9e6 100%)}
.hero-title{left:176px;top:404px;color:var(--green);font-size:21px}
.hero-text{left:176px;top:433px;color:#333;font-size:10.5px;line-height:13px}
.dots{left:698px;top:500px;display:flex;gap:6px}
.dots span{width:11px;height:11px;border-radius:50%;background:var(--green)}
.dots span:first-child{background:var(--orange)}
.feature{width:180px;text-align:center}
.feature .ring{width:72px;height:72px;border:1px solid var(--green);border-radius:50%;margin:0 auto;display:flex;align-items:center;justify-content:center}
.feature h3{font-weight:normal;color:var(--orange);font-size:11px;margin-top:10px}
.feature p{font-size:7.5px;text-align:left;line-height:9.5px;margin-top:4px;padding:0 10px}
.welcome{left:176px;top:725px;font-size:20px;color:var(--green);line-height:23px}
.welcome span{display:block;color:var(--orange);font-size:17.5px}
.photo{left:178px;top:785px;width:167px;height:166px;background:linear-gradient(160deg,#dfe8c0,#b5cd6a 60%,#8eab3a)}
.body-copy{left:362px;top:784px;width:180px;font-size:8px;line-height:10px;color:#444}
.body-copy p{margin-bottom:9px}
.body-copy a{color:var(--orange);text-decoration:none}
.consult{left:577px;top:726px;width:183px;height:227px;background:var(--dark);border-radius:3px}
.consult-head{left:584px;top:719px;width:169px;height:49px}
.consult-title{left:577px;top:728px;width:183px;text-align:center;color:var(--white);font-size:14px}
.consult-title small{display:block;color:#e7f0c8;font-size:7.5px;margin-top:1px}
.field{left:586px;width:166px;height:20px;background:var(--field);border-radius:2px;font-size:8px;color:#555;padding:5px 8px}
.submit{left:586px;top:918px;width:76px;height:23px;background:var(--orange);color:var(--white);font-size:8.5px;text-align:center;line-height:23px;border-radius:2px}
.footer{left:0;top:986px;width:935px;height:214px;background:var(--dark)}
.foot-title{top:1018px;color:var(--orange);font-size:14px}
.foot-item{left:176px;display:flex;gap:9px;color:#ccc;font-size:8px;line-height:10px}
.foot-item svg{flex:none}
.map{left:396px;top:1045px;width:144px;height:96px;border:2px solid #888;background:linear-gradient(135deg,#e8e6df,#d7dde0)}
.hours{left:613px;top:1041px;font-size:8px;color:#fff;line-height:11.7px;border-collapse:collapse}
.hours td{padding:0}
.hours td:first-child{width:52px}
.bottom{left:0;top:1166px;width:935px;height:30px;background:var(--green);color:var(--white);font-size:8px}
.bottom .l{position:absolute;left:176px;top:11px}
.bottom .r{position:absolute;right:182px;top:10px}
</style>
</head>
<body>
<header class="abs header"></header>
<div class="abs brand">
  <span class="brand-mark"></span>
  <div><div class="brand-name">Verdant Vale</div><div class="brand-sub">Chiropractic Health Center</div></div>
</div>
<div class="abs social"><span></span><span></span><span></span><span></span></div>
<div class="abs appt"><svg width="9" height="7" viewBox="0 0 9 7"><path d="M0 3.5h8M5 .5l3 3-3 3" stroke="#dc9d2c" fill="none"/></svg>MAKE AN APPOINTMENT</div>
<div class="abs contact-line" style="top:65px">Address: <b>4182 Maple Fern Court, #305 Chanhassen, MN 55492</b></div>
<div class="abs contact-line" style="top:77px">Phone Number: <b>555-314-2760</b></div>

<nav class="abs nav">
  <a href="#">Home</a><a href="#">Meet Our Staff</a><a href="#">Patient Testimonials</a><a href="#">Videos</a><a href="#">Work Place Wellness</a><a href="#">Contact</a>
</nav>

<div class="abs hero" role="img" aria-label="Banner photo: a smiling young girl touching a pregnant mother's belly"></div>
<div class="abs hero-title">LOROM IPSUM DOLOR SIMET</div>
<div class="abs hero-text">Ut enim ad minim veniam, quis nostrud exercitation<br>ullamco laboris nisi ut aliquip ex ea commodo consequat.</div>
<div class="abs dots"><span></span><span></span><span></span><span></span></div>

<div class="abs feature" style="left:188px;top:554px">
  <div class="ring"><svg width="30" height="30" viewBox="0 0 30 30"><path d="M6 26C4 14 12 5 26 4 27 18 18 26 6 26Z M7 25 20 11" stroke="#7fad1f" stroke-width="2" fill="none"/></svg></div>
  <h3>HEALTH &amp; WELLNESS</h3>
  <p>Duis aute irure dolor in reprehenderit in vouptat velit esse cillum dolore eu fugiat nulla pariatur.</p>
</div>
<div class="abs feature" style="left:378px;top:554px">
  <div class="ring"><svg width="30" height="30" viewBox="0 0 30 30"><path d="M15 4c4 5 3 8 0 10-3-2-4-5 0-10Z" fill="#7fad1f"/><rect x="7" y="16" width="16" height="7" rx="2" fill="#7fad1f"/></svg></div>
  <h3>THERAPEUTIC TREATMENT</h3>
  <p>Duis aute irure dolor in reprehenderit in volutate velit esse cillum dolore eu fugiat nulla pariatur.</p>
</div>
<div class="abs feature" style="left:573px;top:554px">
  <div class="ring"><svg width="30" height="30" viewBox="0 0 30 30" fill="#7fad1f"><ellipse cx="15" cy="6" rx="4" ry="2.5"/><ellipse cx="15" cy="12" rx="7" ry="3"/><ellipse cx="15" cy="18.5" rx="9" ry="3.2"/><ellipse cx="15" cy="25" rx="11" ry="3.2"/></svg></div>
  <h3>MESSAGE THERPAY</h3>
  <p>Duis aute irure dolor in reprehenrit in voluptate velit esse cillum dolore eu fugiat nulla pariatur.</p>
</div>

<h1 class="abs welcome" style="font-weight:normal">WELCOME TO VERDANT VALE<span>CHIROPRACTIC HEALTH CENTER WEBSITE</span></h1>
<div class="abs photo" role="img" aria-label="Photo of a mother holding her baby in a sunny meadow"></div>
<div class="abs body-copy">
  <p>Lorem ipsum dolor sit amet, consectetur adipiscing elit, sed do eiusmod tempor incidunt ut labore et dolore magna aliqua. Ut enim ad minim veiam, quis nosrud exercitation ullamco laboris nisi ut aliquip ex ea coodo consequat.</p>
  <p>Duis aute iure dolor in reprehenrit in voluptate velit esse cillum dolore eu fugiat nulla pariatur. Excepteur sint occaec cupidatat non proident, sunt in culpa qui officia deserunt mollit anim id est laborum.</p>
  <a href="#">read more</a>
</div>

<div class="abs consult"></div>
<svg class="abs consult-head" viewBox="0 0 169 49"><path d="M0 0H169V34L95 44 84 49 73 44 0 34Z" fill="#7fad1f"/><path d="M0 0H169V3H0Z" fill="#9bc93a"/></svg>
<div class="abs consult-title">FREE CONSULTATION<small>CONTACT US TODAY!</small></div>
<div class="abs field" style="top:778px">First Name</div>
<div class="abs field" style="top:801px">Last Name</div>
<div class="abs field" style="top:825px">Phone Number</div>
<div class="abs field" style="top:848px;height:61px">Comments</div>
<div class="abs submit">Submit</div>

<footer class="abs footer"></footer>
<div class="abs foot-title" style="left:175px">CONTACT US</div>
<div class="abs foot-title" style="left:393px">GET DIRECTIONS</div>
<div class="abs foot-title" style="left:612px">OFFICE HOURS</div>
<div class="abs foot-item" style="top:1050px"><svg width="10" height="12" viewBox="0 0 10 12"><path d="M5 12C1 7 0 5.5 0 4.5a5 5 0 0 1 10 0C10 5.5 9 7 5 12Z" fill="#fff"/><circle cx="5" cy="4.5" r="2" fill="#1f1f1f"/></svg><span>4182 Maple Fern Court, #305<br>Chanhassen, MN 55492</span></div>
<div class="abs foot-item" style="top:1079px"><svg width="10" height="10" viewBox="0 0 10 10"><path d="M2 0 4 3 3 4.5Q5 7 6 7L7 6 10 8 8.5 10Q1 8 0 1.5Z" fill="#fff"/></svg><span>555-314-2760</span></div>
<div class="abs foot-item" style="top:1098px"><svg width="10" height="8" viewBox="0 0 10 8"><rect width="10" height="8" fill="#fff"/><path d="M0 0 5 4 10 0" stroke="#1f1f1f" fill="none"/></svg><span>info@verdantvale.com</span></div>
<div class="abs map" role="img" aria-label="Street map showing the clinic location"></div>
<table class="abs hours">
  <tr><td>Monday:</td><td>8:00-11:00, 2:00-5:00</td></tr>
  <tr><td>Tuesday:</td><td>8:30-11:00, 2:00-5:30</td></tr>
  <tr><td>Wednesday:</td><td>8:00-11:00, 2:00-5:00</td></tr>
  <tr><td>Thursday:</td><td>10:00-12:00, 2:30-5:00</td></tr>
  <tr><td>Friday:</td><td>8:00-10:00, 1:00-5:00</td></tr>
  <tr><td>Saturday:</td><td>Closed</td></tr>
  <tr><td>Sunday:</td><td>Closed</td></tr>
</table>
<div class="abs bottom"><span class="l">Copyright ©2015 VerdantVale. All Rights Reserved.</span><span class="r">Powered by Brightpath Site Co</span></div>
</body>
</html>
```